business cards

we want our logos on the back
the information on it are on the design I've uploaded
come up with whatever you think is best, we want something professional, sophisticated and sleek.

```html
<!DOCTYPE html>
<html lang="en">
<head>
<meta charset="utf-8">
<title>Summit Motion Health – Business Cards</title>
<link href="https://fonts.googleapis.com/css2?family=Montserrat:wght@400;500;800&display=swap" rel="stylesheet">
<style>
  :root {
    --stage: #2b2b2b;
    --card: #1d1d1d;
    --card-back: #1a1a1a;
    --pattern-a: #232323;
    --pattern-b: #2c2c2c;
    --white: #f4f4f4;
    --green: #2fe01f;
    --rule: #d8d8d8;
  }
  * { box-sizing: border-box; margin: 0; padding: 0; }
  html, body { width: 1200px; height: 694px; overflow: hidden; }
  body {
    background: var(--stage);
    font-family: "Montserrat", sans-serif;
    color: var(--white);
    position: relative;
  }
  .card {
    position: absolute;
    top: 182px;
    width: 540px;
    height: 330px;
    border-radius: 3px;
    overflow: hidden;
    box-shadow: 0 18px 40px rgba(0,0,0,.45);
  }
  /* Back */
  .card--back { left: 36px; background: var(--card-back); }
  .back-pattern {
    position: absolute; inset: 0;
    background: linear-gradient(135deg, var(--pattern-a) 0%, var(--pattern-b) 60%, var(--pattern-a) 100%);
  }
  .back-brand {
    position: absolute; inset: 0;
    display: flex; align-items: center; justify-content: center; gap: 10px;
  }
  .brand-mark { width: 10px; height: 10px; background: var(--green); }
  .brand-name {
    font-weight: 500; font-size: 20px; letter-spacing: 5px;
    text-transform: uppercase; color: var(--white);
  }
  /* Front */
  .card--front { left: 624px; background: var(--card); }
  .front-decoration {
    position: absolute; right: 0; top: 0; width: 230px; height: 250px;
    background: linear-gradient(120deg, rgba(255,255,255,0) 0%, rgba(255,255,255,.05) 50%, rgba(255,255,255,0) 100%);
  }
  .front-content { position: absolute; left: 36px; top: 30px; right: 36px; }
  .front-brand { display: flex; align-items: center; gap: 8px; margin-bottom: 22px; }
  .front-brand .brand-name { font-size: 17px; letter-spacing: 4px; }
  .person-name { font-weight: 800; font-size: 26px; color: var(--green); line-height: 1.05; margin-bottom: 8px; }
  .credentials { list-style: none; font-size: 12.5px; line-height: 1.5; }
  .credentials .role { text-transform: uppercase; }
  .divider { height: 1px; background: var(--rule); margin: 14px 0 12px; }
  .contacts { display: grid; grid-template-columns: 150px 1fr; gap: 6px 16px; font-size: 12px; }
  .contact { display: flex; align-items: center; gap: 8px; white-space: nowrap; }
  .contact svg { width: 14px; height: 14px; fill: var(--green); flex: none; }
</style>
</head>
<body>

<section class="card card--back" aria-label="Card back">
  <div class="back-pattern" role="img" aria-label="Tonal embossed pattern of the brand symbol repeated across the card"></div>
  <div class="back-brand">
    <span class="brand-mark"></span>
    <span class="brand-name">Summit Motion</span>
  </div>
</section>

<section class="card card--front" aria-label="Card front">
  <div class="front-decoration" role="img" aria-label="Large faint brand symbol watermark"></div>
  <div class="front-content">
    <div class="front-brand">
      <span class="brand-mark"></span>
      <span class="brand-name">Summit Motion</span>
    </div>
    <h1 class="person-name">Daniel Marlow</h1>
    <ul class="credentials">
      <li class="role">Director</li>
      <li class="role">Senior Physiotherapist</li>
      <li>BHlthSc, MPhysioPrac, MExSc(S&amp;C)</li>
      <li>SCC Level 2</li>
    </ul>
    <div class="divider"></div>
    <div class="contacts">
      <div class="contact">
        <svg viewBox="0 0 16 16" aria-hidden="true"><path d="M3 1h3l1.5 4-2 1.3a8 8 0 0 0 4.2 4.2L11 8.5l4 1.5v3a2 2 0 0 1-2 2A12 12 0 0 1 1 3a2 2 0 0 1 2-2z"/></svg>
        <span>03 9000 4817</span>
      </div>
      <div class="contact">
        <svg viewBox="0 0 16 16" aria-hidden="true"><path d="M1 3h14v10H1z M2 4v.4l6 4.2 6-4.2V4z" fill-rule="evenodd"/></svg>
        <span>daniel@summitmotionhealth.com.au</span>
      </div>
      <div class="contact">
        <svg viewBox="0 0 16 16" aria-hidden="true"><path d="M5 1h6a1 1 0 0 1 1 1v12a1 1 0 0 1-1 1H5a1 1 0 0 1-1-1V2a1 1 0 0 1 1-1zm0 2v9h6V3zm3 10a.8.8 0 1 0 0 .1z"/></svg>
        <span>03 9000 5936</span>
      </div>
      <div class="contact">
        <svg viewBox="0 0 16 16" aria-hidden="true"><path d="M8 1a5 5 0 0 1 5 5c0 3.5-5 9-5 9S3 9.5 3 6a5 5 0 0 1 5-5zm0 3a2 2 0 1 0 0 4 2 2 0 0 0 0-4z"/></svg>
        <span>12 Linden St, Riverbend</span>
      </div>
    </div>
  </div>
</section>

</body>
</html>
```